We need a design for a clothing tag for our summer hats & sandals line. Tag should be 2.25" high by 2" wide with a little hole punch circle in the top center. The brand is "Coral Drift" so it should have that name on the tag & then I would also like "Summer Apparel" on the tag somewhere lower on the tag perhaps in a bit smaller font. It should obviously be summer themed- with a picture of a beach or sand- something to that effect. Our previous brand was "Lumen Days"- I have attached that artwork so you can get an idea of what we are looking for.

Logo Text

Coral Drift

```html
<!DOCTYPE html>
<html lang="en">
<head>
<meta charset="utf-8">
<title>Coral Drift — Summer Apparel Tag</title>
<link rel="stylesheet" href="https://fonts.googleapis.com/css2?family=Carlito:wght@400;700&display=swap">
<style>
  :root {
    --backdrop: #0c1614;
    --backdrop-edge: #050908;
    --tag-border: #2b2b2e;
    --sky-top: #2a6ee0;
    --sky-mid: #4ea3ec;
    --sky-low: #8fcdf2;
    --cloud: #d8eefa;
    --sea: #37c9d2;
    --shore: #bfe8e4;
    --sand-light: #f2d6b6;
    --sand: #eec3a0;
    --hole: #0d1413;
    --brand-blue: #0b78c9;
    --ink: #0a0a0a;
  }
  html, body {
    margin: 0;
    padding: 0;
    width: 1200px;
    height: 1062px;
    overflow: hidden;
  }
  body {
    position: relative;
    background: radial-gradient(ellipse at center, var(--backdrop) 55%, var(--backdrop-edge) 100%);
  }
  .hang-tag {
    position: absolute;
    left: 331px;
    top: 227px;
    width: 595px;
    height: 670px;
    border: 3px solid var(--tag-border);
    overflow: hidden;
  }
  .beach-scene {
    position: absolute;
    inset: 0;
    background: linear-gradient(to bottom,
      var(--sky-top) 0%,
      var(--sky-mid) 24%,
      var(--sky-low) 40%,
      var(--cloud) 54%,
      var(--cloud) 62%,
      var(--sea) 65%,
      var(--sea) 70%,
      var(--shore) 73%,
      var(--sand-light) 76%,
      var(--sand) 100%);
  }
  .punch-hole {
    position: absolute;
    left: 270px;
    top: 37px;
    width: 52px;
    height: 52px;
    border-radius: 50%;
    background: var(--hole);
    border: 3px solid var(--tag-border);
  }
  .brand-name {
    position: absolute;
    inset: 0;
    margin: 0;
    font-family: "Carlito", sans-serif;
    font-weight: 700;
    color: var(--brand-blue);
    font-size: 140px;
    line-height: 1;
  }
  .brand-name .line-one {
    position: absolute;
    left: 136px;
    top: 196px;
    white-space: nowrap;
  }
  .brand-name .line-two {
    position: absolute;
    left: 256px;
    top: 356px;
    white-space: nowrap;
  }
  .tagline {
    position: absolute;
    left: 81px;
    top: 570px;
    margin: 0;
    font-family: "Carlito", sans-serif;
    font-weight: 400;
    font-size: 57px;
    line-height: 1;
    color: var(--ink);
    white-space: nowrap;
  }
</style>
</head>
<body>
  <div class="hang-tag">
    <div class="beach-scene" role="img" aria-label="Tropical beach photo: blue sky with white clouds, a small palm-tree island on a turquoise sea, and rippled sand in the foreground"></div>
    <div class="punch-hole"></div>
    <h1 class="brand-name">
      <span class="line-one">Coral</span>
      <span class="line-two">Drift</span>
    </h1>
    <p class="tagline">Summer Apparel</p>
  </div>
</body>
</html>
```